Redesign of business card for Birchline Mechanical

We are looking for a new design for our business cards for Birchline Mechanical. We are a plumbing & HVAC construction company, operating on the West Coast of Canada and USA. Logo attached.
Industry/Entity Type
Construction - Plumbing & HVAC
Contact Information for Business Card
Name, address, phone numbers, email, website address
Look and feel
Each slider illustrates characteristics of the customer's brand and the style your logo design should communicate.

```html
<!DOCTYPE html>
<html lang="en">
<head>
<meta charset="UTF-8">
<title>Birchline Mechanical — Business Card</title>
<link href="https://fonts.googleapis.com/css2?family=Poppins:wght@300;400;600;700&display=swap" rel="stylesheet">
<style>
  :root {
    --backdrop: #212121;
    --card: #1e1f22;
    --card-back: #1c1d21;
    --ink: #ffffff;
    --ink-soft: #e6e6e6;
    --emboss: #2c2d31;
  }
  * { margin: 0; padding: 0; box-sizing: border-box; }
  html, body {
    width: 1200px; height: 780px; overflow: hidden;
    background: var(--backdrop);
    font-family: "Poppins", sans-serif;
    color: var(--ink);
  }
  .stage {
    position: relative; width: 1200px; height: 780px;
    display: flex; align-items: center; justify-content: center; gap: 40px;
  }
  .card {
    position: relative; width: 540px; height: 309px;
    box-shadow: 0 18px 40px rgba(0,0,0,.55);
    overflow: hidden;
  }
  .card--front { background: var(--card); }
  .card--back {
    background: var(--card-back);
    display: flex; align-items: center; justify-content: center;
  }

  .brand {
    position: absolute; left: 34px; top: 34px;
    display: flex; align-items: center; gap: 10px;
  }
  .brand__square { width: 16px; height: 16px; background: var(--ink); }
  .brand__name {
    font-weight: 600; font-size: 17px; letter-spacing: .04em;
    text-transform: uppercase; color: var(--ink);
  }

  .person {
    position: absolute; left: 34px; top: 100px;
    padding-left: 14px; border-left: 8px solid var(--ink);
  }
  .person__name { font-size: 25px; line-height: 1.1; font-weight: 300; }
  .person__name strong { font-weight: 700; }
  .person__title { font-size: 13px; font-weight: 400; color: var(--ink-soft); margin-top: 2px; }

  .address {
    position: absolute; left: 56px; top: 182px;
    font-size: 12px; font-weight: 300; line-height: 1.45; color: var(--ink-soft);
    font-style: normal;
  }
  .contacts {
    position: absolute; left: 36px; top: 228px;
    list-style: none; font-size: 12px; font-weight: 300; color: var(--ink-soft);
  }
  .contacts li { display: flex; align-items: center; gap: 8px; line-height: 1.5; }
  .contacts svg { width: 12px; height: 12px; fill: var(--ink); flex: none; }

  .back-name {
    font-weight: 600; font-size: 30px; letter-spacing: .06em;
    text-transform: uppercase; color: var(--emboss);
    text-shadow: none;
  }
</style>
</head>
<body>
<main class="stage">
  <section class="card card--front" aria-label="Business card front">
    <div class="brand">
      <span class="brand__square"></span>
      <span class="brand__name">Birchline Mechanical</span>
    </div>

    <div class="person">
      <p class="person__name"><strong>Mara</strong> Velinsky</p>
      <p class="person__title">Founder &amp; CEO</p>
    </div>

    <address class="address">
      1840 Harbor Ridge Rd. Suite 310<br>
      Tacoma, WA 98402
    </address>

    <ul class="contacts">
      <li>
        <svg viewBox="0 0 24 24" aria-hidden="true"><path d="M6.6 10.8a15.1 15.1 0 0 0 6.6 6.6l2.2-2.2a1 1 0 0 1 1-.25 11.4 11.4 0 0 0 3.6.57 1 1 0 0 1 1 1V20a1 1 0 0 1-1 1A17 17 0 0 1 3 4a1 1 0 0 1 1-1h3.5a1 1 0 0 1 1 1c0 1.25.2 2.46.57 3.6a1 1 0 0 1-.25 1z"/></svg>
        (253) 555-0147
      </li>
      <li>
        <svg viewBox="0 0 24 24" aria-hidden="true"><path d="M3 5h18a1 1 0 0 1 1 1v12a1 1 0 0 1-1 1H3a1 1 0 0 1-1-1V6a1 1 0 0 1 1-1zm9 7.5L4 7.3V9l8 5 8-5V7.3z"/></svg>
        info@birchlinemech.com
      </li>
      <li>
        <svg viewBox="0 0 24 24" aria-hidden="true"><path d="M12 2a10 10 0 1 0 0 20 10 10 0 0 0 0-20zm6.9 6h-2.9a15 15 0 0 0-1.4-3.6A8 8 0 0 1 18.9 8zM12 4c.8 1.2 1.5 2.5 1.9 4h-3.8c.4-1.5 1.1-2.8 1.9-4zM4.3 14a8 8 0 0 1 0-4h3.4a16 16 0 0 0 0 4zm.8 2h2.9c.3 1.3.8 2.5 1.4 3.6A8 8 0 0 1 5.1 16zM8 8H5.1a8 8 0 0 1 4.3-3.6C8.8 5.5 8.3 6.7 8 8zm4 12c-.8-1.2-1.5-2.5-1.9-4h3.8c-.4 1.5-1.1 2.8-1.9 4zm2.3-6H9.7a14 14 0 0 1 0-4h4.6a14 14 0 0 1 0 4zm.3 5.6c.6-1.1 1.1-2.3 1.4-3.6h2.9a8 8 0 0 1-4.3 3.6zm1.7-5.6a16 16 0 0 0 0-4h3.4a8 8 0 0 1 0 4z"/></svg>
        www.birchlinemech.com
      </li>
    </ul>
  </section>

  <section class="card card--back" aria-label="Business card back">
    <p class="back-name">Birchline Mechanical</p>
  </section>
</main>
</body>
</html>
```